Open Red Harbor.. a non profit that seeks to stomp out skin cancer .. quiet paths toward opening red

Simple letterhead incorporating logo

Industry/Entity Type

Non Profit

Font styles to use
Sans Serif

Colors

Designer to choose colors to be used in the design.

```html
<!DOCTYPE html>
<html lang="en">
<head>
<meta charset="utf-8">
<title>Open Red Harbor – Stationery</title>
<link href="https://fonts.googleapis.com/css2?family=Nunito:wght@400;700&display=swap" rel="stylesheet">
<style>
  :root {
    --navy: #0f1a4a;
    --yellow: #f2f20a;
    --white: #ffffff;
    --paper-shadow: rgba(0,0,0,0.28);
  }
  * { margin: 0; padding: 0; box-sizing: border-box; }
  html, body { width: 1200px; height: 1000px; overflow: hidden; background: var(--white); }
  body { position: relative; font-family: "Nunito", sans-serif; color: var(--navy); }

  .sheet { position: absolute; background: var(--white); box-shadow: 1px 2px 4px var(--paper-shadow); overflow: hidden; }

  /* Letterhead */
  .letterhead { left: 89px; top: 99px; width: 573px; height: 809px; }
  .letterhead__band { position: absolute; left: 0; top: 0; width: 573px; height: 200px; }
  .brand-mark { position: absolute; display: flex; align-items: center; justify-content: center; border: 3px solid var(--yellow); border-radius: 50%; color: var(--yellow); font-weight: 400; text-align: center; line-height: 1.1; }
  .letterhead .brand-mark { left: 55px; top: 33px; width: 102px; height: 102px; font-size: 15px; }
  .letterhead__title { position: absolute; left: 182px; top: 56px; color: var(--white); font-size: 20px; font-weight: 700; letter-spacing: 3px; }
  .letterhead__tagline { position: absolute; left: 182px; top: 87px; color: var(--white); font-size: 9px; line-height: 12px; }

  /* Business card front */
  .card-front { left: 719px; top: 384px; width: 410px; height: 238px; }
  .card-front__art { position: absolute; left: 0; top: 0; }
  .card-front .brand-mark { left: 305px; top: 24px; width: 74px; height: 74px; background: var(--navy); font-size: 10px; }
  .card-front__name { position: absolute; left: 29px; top: 77px; font-size: 15px; }
  .card-front__role { position: absolute; left: 29px; top: 100px; font-size: 12px; }
  .contact-list { position: absolute; left: 29px; top: 145px; list-style: none; font-size: 12px; }
  .contact-list li { display: flex; align-items: center; height: 19px; }
  .contact-list svg { width: 16px; height: 16px; margin-right: 9px; fill: var(--navy); }

  /* Business card back */
  .card-back { left: 719px; top: 670px; width: 410px; height: 238px; background: var(--navy); }
  .card-back__art { position: absolute; left: 0; top: 0; }
  .card-back .brand-mark { left: 150px; top: 54px; width: 112px; height: 112px; font-size: 15px; }
</style>
</head>
<body>

<section class="sheet letterhead">
  <svg class="letterhead__band" viewBox="0 0 573 200">
    <path d="M0,0 H573 V85 Q250,232 0,146 Z" fill="var(--yellow)"/>
    <path d="M0,0 H573 V76 Q250,218 0,139 Z" fill="var(--navy)"/>
  </svg>
  <div class="brand-mark">Open<br>Red<br>Harbor</div>
  <h1 class="letterhead__title">Open Red Harbor</h1>
  <p class="letterhead__tagline">Open Red Harbor..<br>a non profit that seeks to stomp out skin cancer ..<br>quiet paths toward opening red</p>
</section>

<section class="sheet card-front">
  <svg class="card-front__art" width="410" height="238" viewBox="0 0 410 238">
    <circle cx="5" cy="-55" r="110" fill="none" stroke="var(--navy)" stroke-width="3"/>
    <circle cx="445" cy="210" r="103" fill="var(--navy)" stroke="var(--yellow)" stroke-width="7"/>
  </svg>
  <div class="brand-mark">Open<br>Red<br>Harbor</div>
  <p class="card-front__name">Your Name here</p>
  <p class="card-front__role">Title here</p>
  <ul class="contact-list">
    <li><svg viewBox="0 0 16 16"><path d="M8 1a5 5 0 0 0-5 5c0 4 5 9 5 9s5-5 5-9a5 5 0 0 0-5-5zm0 7a2 2 0 1 1 0-4 2 2 0 0 1 0 4z"/></svg>Address: To be confirmed</li>
    <li><svg viewBox="0 0 16 16"><path d="M5 1h6a1 1 0 0 1 1 1v12a1 1 0 0 1-1 1H5a1 1 0 0 1-1-1V2a1 1 0 0 1 1-1zm0 2v9h6V3z"/></svg>Phone: To be confirmed</li>
    <li><svg viewBox="0 0 16 16"><path d="M1 5h3v10H1zM5 6h10v9H5zm2-5h6v4H7zm0 7v2h2V8zm4 0v2h2V8zm-4 3v2h2v-2zm4 0v2h2v-2z"/></svg>Fax: To be confirmed</li>
    <li><svg viewBox="0 0 16 16"><path d="M1 4h14v9H1zm1 1 6 4 6-4z"/></svg>Email: mara@quietharbornet.org.au</li>
  </ul>
</section>

<section class="sheet card-back">
  <svg class="card-back__art" width="410" height="238" viewBox="0 0 410 238">
    <circle cx="20" cy="72" r="95" fill="none" stroke="var(--yellow)" stroke-width="3"/>
    <circle cx="70" cy="285" r="100" fill="none" stroke="var(--yellow)" stroke-width="1.5"/>
    <circle cx="455" cy="200" r="130" fill="none" stroke="var(--yellow)" stroke-width="10"/>
  </svg>
  <div class="brand-mark">Open<br>Red<br>Harbor</div>
</section>

</body>
</html>
```